Business Card for Coach - ready to print

Design Business Card ready to order prints www.lukasbrenner.coach

* An Overview / Background of the Business & Services
· Coaching
· Personal growth
* The Target Market / Audience you are trying to reach
· private person in different roles (self, familiy, business role)s
* Design Specifics; any preferences or ideas for Style, Colour, Imagery, etc
· See www.lukasbrenner.coach
· "simple" design
· (small) element of surprise / unusual element

* Information that will be placed in the Business Card
· Beratung und Coaching
· Address: Lukas Brenner, Talmatt 42, CH-8531 Winterthur, Mobile +41 76 254 63 07
* Do you have an existing website or Facebook page where designers can learn more about your company?
· lukasbrenner.coach

Target Market(s)

private person in different roles (self, familiy, business role)

Industry/Entity Type

Life Coaching

Contact Information for Business Card

Lukas Brenner
Talmatt 42
CH-8531 Winterthur

Mobile: +41 76 254 63 07
Email: lubr@sonnwelt.ch
www.lukasbrenner.coach

Font styles to use
Sans Serif

Colors

Designer to choose colors to be used in the design.

Requirements
Must have
• "simple" design
• element of surprise / unusual element
• Beratung & Coaching
• see www.lukasbrenner.coach for colors and so...
Nice to have
• TA Symbol (three rings on top of each other) - unsual presentation
• QR Code of Website (see if it fits in and still looks good).

```html
<!DOCTYPE html>
<html lang="de">
<head>
<meta charset="utf-8">
<title>Lukas Brenner – Beratung and Coaching</title>
<link rel="stylesheet" href="https://fonts.googleapis.com/css2?family=Lato:wght@400;700;900&display=swap">
<style>
  :root {
    --page: #d9dadb;
    --card: #1d1d1f;
    --accent: #5bc3e0;
    --text: #c4c4c4;
    --muted: #9a9a9a;
    --rule: #6a6a6a;
    --portrait-a: #b9bcbf;
    --portrait-b: #8e9296;
  }
  * { box-sizing: border-box; margin: 0; padding: 0; }
  html, body { width: 1200px; height: 900px; overflow: hidden; }
  body {
    background: var(--page);
    display: flex;
    align-items: center;
    justify-content: center;
    font-family: "Lato", sans-serif;
  }
  .card {
    width: 440px;
    height: 760px;
    background: var(--card);
    border-radius: 4px;
    box-shadow: 0 18px 40px rgba(0,0,0,.25);
    display: flex;
    flex-direction: column;
    align-items: center;
    padding-top: 70px;
    color: var(--text);
    text-align: center;
  }
  .portrait {
    width: 220px;
    height: 220px;
    border-radius: 50%;
    border: 3px solid var(--accent);
    background: radial-gradient(circle at 50% 40%, var(--portrait-a), var(--portrait-b));
  }
  .name {
    margin-top: 42px;
    color: var(--accent);
    font-weight: 900;
    font-size: 40px;
    letter-spacing: 1px;
    line-height: 1;
  }
  .role {
    margin-top: 8px;
    font-size: 22px;
    color: var(--text);
  }
  .rule {
    width: 240px;
    height: 1px;
    background: var(--rule);
    margin: 18px 0;
  }
  .rule-icons {
    position: relative;
    display: flex;
    justify-content: center;
    align-items: center;
    width: 240px;
    margin: 16px 0;
  }
  .rule-icons::before {
    content: "";
    position: absolute;
    left: 0; right: 0; top: 50%;
    height: 1px;
    background: var(--rule);
  }
  .icons { position: relative; display: flex; gap: 4px; background: var(--card); padding: 0 6px; }
  .icon { width: 24px; height: 24px; }
  .contact p { font-size: 21px; line-height: 1.38; color: var(--text); }
  .company p { font-size: 21px; line-height: 1.3; color: var(--muted); }
  .company .firm { color: var(--accent); }
  .services p { font-size: 21px; line-height: 1.3; color: var(--muted); }
</style>
</head>
<body>
  <main class="card">
    <div class="portrait" role="img" aria-label="Round portrait photo of the coach"></div>
    <h1 class="name">LUKAS BRENNER</h1>
    <p class="role">Founder | CEO</p>

    <div class="rule-icons">
      <div class="icons">
        <svg class="icon" viewBox="0 0 24 24" aria-label="Phone">
          <circle cx="12" cy="12" r="12" fill="var(--accent)"/>
          <path d="M8 6.5c.6-.4 1.3-.3 1.6.3l1 1.8c.3.5.1 1.1-.3 1.4l-.7.5c.5 1.4 1.5 2.5 2.9 3.1l.5-.7c.3-.5 1-.6 1.5-.3l1.8 1c.6.3.7 1 .3 1.6l-.7.9c-.6.7-1.6.9-2.5.5-3-1.3-5.3-3.6-6.5-6.6-.3-.9-.1-1.9.6-2.5z" fill="var(--card)"/>
        </svg>
        <svg class="icon" viewBox="0 0 24 24" aria-label="Email">
          <circle cx="12" cy="12" r="12" fill="var(--accent)"/>
          <rect x="6" y="8" width="12" height="8.5" rx="1" fill="var(--card)"/>
          <path d="M6.5 8.6 12 13l5.5-4.4" stroke="var(--accent)" stroke-width="1.2" fill="none"/>
        </svg>
        <svg class="icon" viewBox="0 0 24 24" aria-label="Website">
          <circle cx="12" cy="12" r="12" fill="var(--accent)"/>
          <circle cx="12" cy="12" r="6.5" fill="none" stroke="var(--card)" stroke-width="1.4"/>
          <ellipse cx="12" cy="12" rx="2.8" ry="6.5" fill="none" stroke="var(--card)" stroke-width="1.2"/>
          <path d="M5.5 12h13M6.5 9h11M6.5 15h11" stroke="var(--card)" stroke-width="1.1"/>
        </svg>
      </div>
    </div>

    <div class="contact">
      <p class="phone">+41 76 254 63 07</p>
      <p class="email">lubr@sonnwelt.ch</p>
      <p class="web">www.lukasbrenner.coach</p>
    </div>

    <div class="rule"></div>

    <div class="company">
      <p class="firm">Beratung and Coaching</p>
      <p>Lukas Brenner, Talmatt 42</p>
      <p>CH-8531 Winterthur</p>
    </div>

    <div class="rule"></div>

    <div class="services">
      <p>Coaching</p>
      <p>Personal growth</p>
    </div>
  </main>
</body>
</html>
```